We are a organisation that provide outdoor adventure based tours to international students in New Ze

We are a Waikato New Zealand based company that runs adventure and outdoor tours around New Zealand. Activities included in our tours are mountain biking, rafting, sea kayaking, surfing/SUPing, luge, high ropes course, tramping, snorkelling and cultural activities. We need a Name/Logo, advertisement and information Flyers that we can give to the students/customers ASAP. We still haven't come up with a name so are hoping that designers can be more creative than we are. we are running our fist trip Dec 15th-22nd 2013.

Attached are some bits of information that we need to be included in the flyer. We need to get the 'Brightwater Tour' filled up first and the 'Kestrel's Cove Tour' will be later.

We want it to be an exciting and edgy design with an 'outdoor' feel to it. There is the potential for this design to be expanded into our website.

The brochure/ Flyer can come in any creative format.

Target Market(s)

High school aged students. We will be expanding to University students in the future. We also need to make sure that this is appealing to the parents. It will be them who will agree to them going on the trips after all.

Industry/Entity Type

It Company

Requirements
Must have
• Our Contact details.
Booking Info
Tour information from attached.
Nice to have
• Photos can use the ones we have put into the attachment or other images from the outdoors that designers can source to make it look good.

```html
<!DOCTYPE html>
<html lang="en">
<head>
<meta charset="utf-8">
<title>Kestrel's Cove Tour – Tidewild Adventures</title>
<link rel="stylesheet" href="https://fonts.googleapis.com/css2?family=Open+Sans:wght@400;600;700;800&family=Oswald:wght@500;600;700&family=PT+Serif:wght@700&family=Noto+Serif:ital,wght@1,700&family=Kaushan+Script&display=swap">
<style>
:root{
  --stage:#4a4d50;
  --paper:#ffffff;
  --teal:#1b9fc6;
  --teal-deep:#0f86b0;
  --green:#8cc63f;
  --orange:#f7941d;
  --orange-deep:#f0820f;
  --yellow:#fff200;
  --title-yellow:#f7e81c;
  --red:#e8453c;
  --navy:#1d2a6b;
  --grey-text:#555a5e;
  --ink:#222;
  --price-green:#5cb846;
  --pink:#e6197e;
  --brand-blue:#1560a8;
}
*{margin:0;padding:0;box-sizing:border-box}
html,body{width:1200px;height:909px;overflow:hidden;background:var(--stage)}
body{position:relative;font-family:"Open Sans",Arial,sans-serif}
.abs{position:absolute}
.spread{position:absolute;left:60px;top:72px;width:1080px;height:764px;background:var(--paper);overflow:hidden}

/* left page */
.left-head{left:0;top:0}
.tour-title{left:42px;top:22px;font-family:"PT Serif",Georgia,serif;font-size:23px;color:var(--title-yellow);letter-spacing:.3px}
.tour-facts{left:320px;top:14px;list-style:none;color:#fff;font-family:"Oswald",Arial,sans-serif;font-weight:500;font-size:14.5px;line-height:20px}
.tour-facts li::before{content:"";display:inline-block;width:9px;height:9px;background:var(--yellow);margin-right:9px;vertical-align:1px}
.photo{position:absolute}
.ph-swim{left:0;top:78px;width:160px;height:150px;background:linear-gradient(180deg,#7fb7d8 0%,#2f6e9c 45%,#123e63 100%);clip-path:polygon(0 0,100% 0,92% 100%,0 100%)}
.ph-raft{left:148px;top:78px;width:205px;height:150px;background:radial-gradient(circle at 55% 45%,#e9e2d0 0%,#9a8a6a 35%,#4d4a33 75%,#2c2a1e 100%);clip-path:polygon(6% 0,97% 0,90% 100%,0 100%)}
.ph-reef{left:336px;top:78px;width:204px;height:150px;background:linear-gradient(160deg,#4fc3e6 0%,#1c8fc4 50%,#0d4f86 100%);clip-path:polygon(8% 0,100% 0,100% 100%,0 100%)}
.left-orange{left:0;top:208px}
.intro{left:32px;top:255px;width:210px;font-size:12.3px;line-height:16.4px;color:var(--grey-text)}
.activities-title{left:30px;top:388px;font-family:Arial,sans-serif;font-size:15px;line-height:18px;color:var(--red)}
.activity-list{list-style:none;font-size:12px;font-weight:700;color:var(--teal-deep);line-height:15px}
.activity-list li{position:relative;padding-left:22px;margin-bottom:7px}
.activity-list li svg{position:absolute;left:0;top:1px}
.col-a{left:28px;top:436px;width:120px}
.col-b{left:146px;top:436px;width:110px}
.included{left:28px;top:668px;width:218px;height:68px;border:1.5px dashed var(--red);border-radius:10px}
.included-tag{left:114px;top:664px;background:var(--red);color:#fff;font-size:11.5px;font-weight:600;padding:2px 7px}
.included-list{left:38px;top:676px;list-style:none;font-size:11.5px;font-weight:700;color:var(--ink);line-height:18px}
.included-list li{display:flex;align-items:center;gap:8px}

.itinerary{left:260px;top:246px;width:260px;height:492px;background:var(--orange);border-radius:0 14px 14px 14px}
.itin-lead{left:12px;top:14px;width:170px;color:#fff;font-weight:700;font-size:13.2px;line-height:17px}
.price{left:183px;top:-12px;width:78px;height:78px;border-radius:50%;background:var(--price-green);border:3px solid #fff;color:#fff;text-align:center}
.price-amount{display:block;font-family:"Oswald",Arial,sans-serif;font-weight:700;font-size:25px;line-height:26px;margin-top:22px}
.price-note{display:block;font-size:8px;font-weight:600}
.price-sign{left:190px;top:-8px;width:28px;height:28px;border-radius:50%;background:var(--pink);border:2px solid #fff;color:#fff;font-weight:700;font-size:16px;line-height:24px;text-align:center}
.day{position:absolute;left:12px;display:flex;width:240px}
.day-num{width:28px;color:var(--yellow);font-family:"Oswald",Arial,sans-serif;text-align:left;line-height:1}
.day-num small{display:block;font-size:9px;font-weight:600}
.day-num b{display:block;font-size:19px;font-weight:600}
.day-text{border-left:1.5px solid #fff;padding-left:7px;color:#fff;font-size:11.2px;font-weight:700;line-height:14.5px}

/* right page */
.hero{left:540px;top:0;width:540px;height:380px;background:linear-gradient(200deg,#1f3fa3 0%,#4d8fd8 28%,#a9d2f2 45%,#eef6fb 62%,#c9d9e8 100%)}
.book{right:28px;top:20px;text-align:right;color:#fff;font-weight:700}
.book-label{font-size:17px;letter-spacing:.3px;margin-right:30px}
.book-phone{font-size:27px;line-height:30px}
.book-mail{font-size:14px}
.headline{left:620px;top:218px;width:440px;text-align:center;font-family:"Kaushan Script",cursive;font-size:56px;line-height:46px;color:#fff;-webkit-text-stroke:2px var(--navy);paint-order:stroke fill;text-shadow:3px 3px 0 var(--navy);transform:rotate(-6deg)}
.right-band{left:540px;top:356px}
.tagline{left:568px;top:396px;width:290px;font-family:"Noto Serif",Georgia,serif;font-style:italic;font-weight:700;font-size:20px;line-height:24px;color:#fff}
.badge{left:876px;top:356px;width:196px;height:196px;border-radius:50%;background:var(--yellow);border:5px solid #fff;text-align:center}
.badge-text{position:absolute;left:0;right:0;top:62px;font-family:"Oswald",Arial,sans-serif;font-weight:600;font-size:20px;line-height:27px;color:var(--red)}
.badge-amp{display:inline-block;width:22px;height:22px;border-radius:50%;background:var(--pink);color:#fff;font-size:14px;line-height:22px;margin-right:6px;vertical-align:2px}
.ribbon{left:866px;top:342px;width:178px;height:32px;background:var(--red);color:#fff;font-family:"Oswald",Arial,sans-serif;font-weight:600;font-size:21px;line-height:32px;text-align:center;transform:rotate(-4deg);box-shadow:2px 2px 0 rgba(0,0,0,.25)}
.ph-group{left:540px;top:520px;width:200px;height:150px;background:linear-gradient(180deg,#bcd9ea 0%,#7aa0a5 40%,#5e6a58 70%,#3d3a33 100%);clip-path:polygon(0 0,100% 0,93% 100%,0 100%)}
.ph-bay{left:727px;top:520px;width:195px;height:150px;background:linear-gradient(180deg,#c6e1f2 0%,#7fb7d3 35%,#3f7b70 60%,#2f6b2e 100%);clip-path:polygon(7% 0,100% 0,92% 100%,0 100%)}
.ph-rafting{left:906px;top:520px;width:174px;height:150px;background:linear-gradient(170deg,#3a6b3a 0%,#77a6c4 45%,#e9f1f3 70%,#d8b33a 100%);clip-path:polygon(9% 0,100% 0,100% 100%,0 100%)}
.right-orange{left:540px;top:654px}
.brand{left:568px;top:694px;display:flex;align-items:center;gap:8px}
.brand-mark{width:30px;height:30px;background:var(--brand-blue)}
.brand-name{font-family:"Open Sans",Arial,sans-serif;font-weight:700;font-size:15px;line-height:17px;color:var(--brand-blue);width:100px}
.contacts{left:744px;top:692px;list-style:none;border-left:1px solid #999;padding-left:8px;font-size:10.6px;font-weight:700;color:var(--ink);line-height:15.5px}
.contacts li{display:flex;align-items:center;gap:6px}
.contact-person{left:968px;top:697px;border-left:1px solid #999;padding-left:8px;height:56px;font-size:10px;color:var(--ink)}
.contact-person strong{display:block;margin-top:6px;font-size:11px;letter-spacing:.5px}
</style>
</head>
<body>
<main class="spread">

  <!-- LEFT PAGE -->
  <svg class="abs left-head" width="540" height="100" viewBox="0 0 540 100" aria-hidden="true">
    <path d="M0 0H540V62L500 72 460 60 420 72 380 58 340 68 300 56 260 70 220 58 180 70 140 58 100 70 60 60 30 70 0 62Z" fill="var(--teal)"/>
    <path d="M0 62L30 70 60 60 100 70 140 58 180 70 220 58 260 70 300 56 340 68 380 58 420 72 460 60 500 72 540 62V90H0Z" fill="var(--green)"/>
  </svg>
  <h1 class="abs tour-title">KESTREL'S COVE TOUR</h1>
  <ul class="abs tour-facts">
    <li>Tour dates : 23rd -30th Jan</li>
    <li>Limited to 30 spaces</li>
  </ul>

  <div class="photo ph-swim" role="img" aria-label="Photo of a snorkeller in the sea with a boat behind"></div>
  <div class="photo ph-raft" role="img" aria-label="Photo of a raft crew on white water from above"></div>
  <div class="photo ph-reef" role="img" aria-label="Photo of a diver among reef fish"></div>

  <svg class="abs left-orange" width="540" height="30" viewBox="0 0 540 30" aria-hidden="true">
    <path d="M0 6L40 12 80 4 120 14 170 6 220 16 270 6 320 14 370 6 420 16 470 8 540 14V26L480 20 420 28 360 20 300 28 240 20 180 28 120 20 60 28 0 22Z" fill="var(--orange)"/>
  </svg>

  <p class="abs intro">Kestrel's Cove Tour takes you on a Journey to the golden beaches, crystal clear waters and lush native NZ bush of the Coromandel. We then make our way to New Zealands best adventure destinations Rotorua. Through to Taupo and the central plateau where we</p>

  <h2 class="abs activities-title">ACTIVITIES WE HAVE<br>INCLUDED IN THE TOUR ARE:</h2>
  <ul class="abs activity-list col-a">
    <li><svg width="13" height="13" viewBox="0 0 13 13"><circle cx="6.5" cy="6.5" r="5.5" fill="none" stroke="var(--red)" stroke-width="1.6"/><path d="M4 6.5H9M6.8 4.3L9 6.5 6.8 8.7" fill="none" stroke="var(--red)" stroke-width="1.6"/></svg>RAFTING</li>
    <li><svg width="13" height="13" viewBox="0 0 13 13"><circle cx="6.5" cy="6.5" r="5.5" fill="none" stroke="var(--red)" stroke-width="1.6"/><path d="M4 6.5H9M6.8 4.3L9 6.5 6.8 8.7" fill="none" stroke="var(--red)" stroke-width="1.6"/></svg>MOUNTAIN BIKING</li>
    <li><svg width="13" height="13" viewBox="0 0 13 13"><circle cx="6.5" cy="6.5" r="5.5" fill="none" stroke="var(--red)" stroke-width="1.6"/><path d="M4 6.5H9M6.8 4.3L9 6.5 6.8 8.7" fill="none" stroke="var(--red)" stroke-width="1.6"/></svg>LUGE/THRILL RIDES</li>
    <li><svg width="13" height="13" viewBox="0 0 13 13"><circle cx="6.5" cy="6.5" r="5.5" fill="none" stroke="var(--red)" stroke-width="1.6"/><path d="M4 6.5H9M6.8 4.3L9 6.5 6.8 8.7" fill="none" stroke="var(--red)" stroke-width="1.6"/></svg>SEA KAYAKING CATHEDRAL COVE</li>
    <li><svg width="13" height="13" viewBox="0 0 13 13"><circle cx="6.5" cy="6.5" r="5.5" fill="none" stroke="var(--red)" stroke-width="1.6"/><path d="M4 6.5H9M6.8 4.3L9 6.5 6.8 8.7" fill="none" stroke="var(--red)" stroke-width="1.6"/></svg>TRAMPING</li>
    <li><svg width="13" height="13" viewBox="0 0 13 13"><circle cx="6.5" cy="6.5" r="5.5" fill="none" stroke="var(--red)" stroke-width="1.6"/><path d="M4 6.5H9M6.8 4.3L9 6.5 6.8 8.7" fill="none" stroke="var(--red)" stroke-width="1.6"/></svg>GLASS BOTTOM BOAT</li>
  </ul>
  <ul class="abs activity-list col-b">
    <li><svg width="13" height="13" viewBox="0 0 13 13"><circle cx="6.5" cy="6.5" r="5.5" fill="none" stroke="var(--red)" stroke-width="1.6"/><path d="M4 6.5H9M6.8 4.3L9 6.5 6.8 8.7" fill="none" stroke="var(--red)" stroke-width="1.6"/></svg>BUNGY</li>
    <li><svg width="13" height="13" viewBox="0 0 13 13"><circle cx="6.5" cy="6.5" r="5.5" fill="none" stroke="var(--red)" stroke-width="1.6"/><path d="M4 6.5H9M6.8 4.3L9 6.5 6.8 8.7" fill="none" stroke="var(--red)" stroke-width="1.6"/></svg>SNORKELING</li>
    <li><svg width="13" height="13" viewBox="0 0 13 13"><circle cx="6.5" cy="6.5" r="5.5" fill="none" stroke="var(--red)" stroke-width="1.6"/><path d="M4 6.5H9M6.8 4.3L9 6.5 6.8 8.7" fill="none" stroke="var(--red)" stroke-width="1.6"/></svg>FISHING</li>
    <li><svg width="13" height="13" viewBox="0 0 13 13"><circle cx="6.5" cy="6.5" r="5.5" fill="none" stroke="var(--red)" stroke-width="1.6"/><path d="M4 6.5H9M6.8 4.3L9 6.5 6.8 8.7" fill="none" stroke="var(--red)" stroke-width="1.6"/></svg>HIGH ROPES COURSE</li>
    <li><svg width="13" height="13" viewBox="0 0 13 13"><circle cx="6.5" cy="6.5" r="5.5" fill="none" stroke="var(--red)" stroke-width="1.6"/><path d="M4 6.5H9M6.8 4.3L9 6.5 6.8 8.7" fill="none" stroke="var(--red)" stroke-width="1.6"/></svg>HOT POOLS</li>
    <li><svg width="13" height="13" viewBox="0 0 13 13"><circle cx="6.5" cy="6.5" r="5.5" fill="none" stroke="var(--red)" stroke-width="1.6"/><path d="M4 6.5H9M6.8 4.3L9 6.5 6.8 8.7" fill="none" stroke="var(--red)" stroke-width="1.6"/></svg>SIGHT SEEING</li>
    <li><svg width="13" height="13" viewBox="0 0 13 13"><circle cx="6.5" cy="6.5" r="5.5" fill="none" stroke="var(--red)" stroke-width="1.6"/><path d="M4 6.5H9M6.8 4.3L9 6.5 6.8 8.7" fill="none" stroke="var(--red)" stroke-width="1.6"/></svg>CULTURAL EXPERIENCE</li>
  </ul>

  <div class="abs included"></div>
  <span class="abs included-tag">Included in the costs</span>
  <ul class="abs included-list">
    <li><svg width="14" height="12" viewBox="0 0 14 12"><path d="M1 5H13A6 6 0 0 1 1 5Z" fill="var(--pink)"/><path d="M4 1V4M7 0V4M10 1V4" stroke="var(--pink)" stroke-width="1.3"/></svg>Food</li>
    <li><svg width="18" height="12" viewBox="0 0 18 12"><rect x="0" y="1" width="17" height="8" rx="2" fill="var(--pink)"/><circle cx="4" cy="10" r="1.8" fill="var(--pink)"/><circle cx="13" cy="10" r="1.8" fill="var(--pink)"/><rect x="2" y="3" width="4" height="3" fill="#fff"/><rect x="7" y="3" width="4" height="3" fill="#fff"/></svg>All transport</li>
    <li><svg width="16" height="12" viewBox="0 0 16 12"><rect x="0" y="1" width="16" height="10" rx="1.5" fill="var(--pink)"/><text x="8" y="9.5" font-size="8" font-weight="700" fill="#fff" text-anchor="middle" font-family="Arial">$</text></svg>Cost of all activities and guides</li>
  </ul>

  <section class="abs itinerary">
    <p class="abs itin-lead">All of this, 7 days of fun and making memories with other international students for</p>
    <div class="abs price"><span class="price-amount">1399</span><span class="price-note">Per person</span></div>
    <div class="abs price-sign">$</div>

    <div class="day" style="top:88px"><div class="day-num"><small>DAY</small><b>01</b></div><p class="day-text">Waikato high ropes course and travel to Papa Aroha Coromandel for some kiwi camping</p></div>
    <div class="day" style="top:146px"><div class="day-num"><small>DAY</small><b>02</b></div><p class="day-text">Travel to Whitianga and go on the 'Glass Bottom Boat' and Snorkeling in the Marine reserve</p></div>
    <div class="day" style="top:202px"><div class="day-num"><small>DAY</small><b>03</b></div><p class="day-text">Kayak Tours to Cathedral Cove and dig a spa at hotwater beach with fish and chips on the beach</p></div>
    <div class="day" style="top:260px"><div class="day-num"><small>DAY</small><b>04</b></div><p class="day-text">Travel to the Rotorua luge and skyrides. Later hit the geothermal hot pools and 'Cultural Night'</p></div>
    <div class="day" style="top:316px"><div class="day-num"><small>DAY</small><b>05</b></div><p class="day-text">Raft the Kaituna River and Mountain Biking Redwood forests and BBQ night</p></div>
    <div class="day" style="top:358px"><div class="day-num"><small>DAY</small><b>06</b></div><p class="day-text">Travel to Taupo where you have the option to bungy jump and then we go to the mysterious 'Craters of the Moon'</p></div>
    <div class="day" style="top:414px"><div class="day-num"><small>DAY</small><b>07</b></div><p class="day-text">Huka Falls, natural hot springs and miniputt</p></div>
    <div class="day" style="top:456px"><div class="day-num"><small>DAY</small><b>08</b></div><p class="day-text">Travel and farewells</p></div>
  </section>

  <!-- RIGHT PAGE -->
  <div class="abs hero" role="img" aria-label="Photo of a skier carving down a sunlit snowy mountain slope"></div>
  <div class="abs book">
    <p class="book-label">BOOK NOW !</p>
    <p class="book-phone">02 10 555 017</p>
    <p class="book-mail">samharlow@mailbox.co.nz</p>
  </div>
  <p class="abs headline">Take the path<br>less travelled</p>

  <svg class="abs right-band" width="540" height="180" viewBox="0 0 540 180" aria-hidden="true">
    <path d="M0 10L50 4 100 14 150 4 200 16 260 6 320 16 380 6 440 16 490 6 540 12V30H0Z" fill="var(--green)"/>
    <path d="M0 24L50 18 100 28 150 18 200 30 260 20 320 30 380 20 440 30 490 20 540 26V180H0Z" fill="var(--teal)"/>
  </svg>
  <p class="abs tagline">We are the only adventure tour organization providing exciting experiences on and off the beaten track</p>

  <div class="abs badge">
    <p class="badge-text">Brightwater Tour<br><span class="badge-amp">&amp;</span>Kestrel's<br>Cove Tour</p>
  </div>
  <div class="abs ribbon">NEW ZEALAND</div>

  <div class="photo ph-group" role="img" aria-label="Photo of a student group gathered by a lake shore"></div>
  <div class="photo ph-bay" role="img" aria-label="Photo of a calm bay with green bush and hills"></div>
  <div class="photo ph-rafting" role="img" aria-label="Photo of a rafting team paddling through rapids"></div>

  <svg class="abs right-orange" width="540" height="30" viewBox="0 0 540 30" aria-hidden="true">
    <path d="M0 8L60 14 120 4 180 14 240 6 300 16 360 6 420 14 480 4 540 10V22L480 16 420 26 360 18 300 26 240 18 180 26 120 18 60 26 0 20Z" fill="var(--orange)"/>
  </svg>

  <div class="abs brand">
    <span class="brand-mark"></span>
    <span class="brand-name">Tidewild Adventures</span>
  </div>
  <ul class="abs contacts">
    <li><svg width="11" height="8" viewBox="0 0 11 8"><rect x=".5" y=".5" width="10" height="7" fill="none" stroke="var(--teal-deep)"/><path d="M.5 .5L5.5 4.5 10.5 .5" fill="none" stroke="var(--teal-deep)"/></svg>hello@tidewildadventures.co.nz</li>
    <li><svg width="11" height="11" viewBox="0 0 11 11"><circle cx="5.5" cy="5.5" r="4.8" fill="none" stroke="var(--teal-deep)"/><path d="M.7 5.5H10.3M5.5 .7V10.3" stroke="var(--teal-deep)"/><ellipse cx="5.5" cy="5.5" rx="2.2" ry="4.8" fill="none" stroke="var(--teal-deep)"/></svg>tidewildadventures.co.nz</li>
    <li><svg width="11" height="11" viewBox="0 0 11 11"><rect x="2.5" y=".5" width="6" height="10" rx="1" fill="none" stroke="var(--teal-deep)"/><circle cx="5.5" cy="8.7" r=".8" fill="var(--teal-deep)"/></svg>+64 22 555 0193</li>
    <li><svg width="11" height="11" viewBox="0 0 11 11"><circle cx="5.5" cy="5.5" r="5" fill="var(--teal-deep)"/></svg>www.social.net\tidewildadventures</li>
  </ul>
  <div class="abs contact-person">Conatact :<strong>SAM HARLOW</strong></div>
</main>
</body>
</html>
```